Gombrevo business card

Based on company logo and website given , to design a business card temple. Slogan "Your furry friends deserves the best"
Color style please refer to our website

```html
<!DOCTYPE html>
<html lang="en">
<head>
<meta charset="utf-8">
<title>Gombrevo business card</title>
<link rel="stylesheet" href="https://fonts.googleapis.com/css2?family=Bebas+Neue&family=Arimo:wght@400&family=Tinos:wght@400&display=swap">
<style>
  :root {
    --backdrop: #2b2b2d;
    --card: #1d1e20;
    --card-edge: #26272a;
    --gold: #c6b52e;
    --text: #dcdcdc;
    --muted: #bdbdbd;
    --rule: #4a4b4e;
    --pattern-a: #222326;
    --pattern-b: #2e2f33;
    --white: #ffffff;
  }
  * { margin: 0; padding: 0; box-sizing: border-box; }
  html, body { width: 1200px; height: 1108px; overflow: hidden; }
  body {
    background: var(--backdrop);
    position: relative;
    font-family: "Arimo", Arial, sans-serif;
  }
  .card {
    position: absolute;
    top: 189px;
    width: 470px;
    height: 730px;
    background: var(--card);
    border-radius: 26px;
    box-shadow: 0 18px 40px rgba(0,0,0,.45);
    overflow: hidden;
  }
  .card--front { left: 90px; }
  .card--back { left: 640px; }

  .wordmark {
    font-family: "Tinos", "Times New Roman", serif;
    color: var(--gold);
    font-weight: 400;
    text-align: center;
    letter-spacing: -1px;
  }
  .card--front .wordmark { margin-top: 150px; font-size: 86px; line-height: 1; }

  .person { margin-top: 150px; text-align: center; }
  .person__name {
    font-family: "Tinos", "Times New Roman", serif;
    color: var(--gold);
    font-size: 30px;
    letter-spacing: 1px;
  }
  .person__role { color: var(--muted); font-size: 22px; margin-top: 2px; }

  .icon-row {
    display: flex; align-items: center; justify-content: center;
    gap: 8px; margin-top: 16px;
  }
  .icon-row__rule { width: 48px; height: 1px; background: var(--rule); }
  .icon-row__icon { width: 38px; height: 38px; }

  .contact { margin-top: 12px; text-align: center; color: var(--text); font-size: 23px; line-height: 1.32; }
  .divider { width: 300px; height: 1px; background: var(--rule); margin: 16px auto 14px; }
  .address { text-align: center; color: var(--text); font-size: 23px; line-height: 1.32; }

  .pattern-field {
    position: absolute; inset: 0;
    background: linear-gradient(150deg, var(--pattern-b) 0%, var(--pattern-a) 45%, var(--pattern-b) 70%, var(--pattern-a) 100%);
  }
  .card--back .wordmark {
    position: absolute; left: 0; right: 0; top: 300px;
    font-size: 58px; line-height: 1;
  }
  .slogan {
    position: absolute; left: 0; right: 0; top: 520px;
    font-family: "Bebas Neue", Impact, sans-serif;
    color: var(--white);
    font-size: 56px;
    line-height: 1;
    text-align: center;
    letter-spacing: .5px;
  }
</style>
</head>
<body>
  <section class="card card--front">
    <div class="wordmark">Gombrevo</div>
    <div class="person">
      <div class="person__name">DANIEL HARLOW</div>
      <div class="person__role">Managing Director</div>
    </div>
    <div class="icon-row">
      <span class="icon-row__rule"></span>
      <svg class="icon-row__icon" viewBox="0 0 38 38" aria-label="Phone">
        <rect width="38" height="38" rx="7" fill="var(--gold)"/>
        <path d="M9 15c0-3 4-5 10-5s10 2 10 5l-4 1-1-3h-10l-1 3z M12 18h14l2 10H10z" fill="var(--card)"/>
      </svg>
      <svg class="icon-row__icon" viewBox="0 0 38 38" aria-label="Mobile">
        <rect width="38" height="38" rx="7" fill="var(--gold)"/>
        <rect x="13" y="8" width="12" height="22" rx="2" fill="none" stroke="var(--card)" stroke-width="2.4"/>
        <circle cx="19" cy="26" r="1.4" fill="var(--card)"/>
      </svg>
      <svg class="icon-row__icon" viewBox="0 0 38 38" aria-label="Web">
        <rect width="38" height="38" rx="7" fill="var(--gold)"/>
        <circle cx="19" cy="19" r="10" fill="var(--card)"/>
        <path d="M9 19h20M19 9c-4 5-4 15 0 20M19 9c4 5 4 15 0 20" stroke="var(--gold)" stroke-width="1.4" fill="none"/>
      </svg>
      <svg class="icon-row__icon" viewBox="0 0 38 38" aria-label="Email">
        <rect width="38" height="38" rx="7" fill="var(--gold)"/>
        <rect x="8" y="12" width="22" height="15" fill="none" stroke="var(--card)" stroke-width="2.2"/>
        <path d="M8 12l11 9 11-9M8 27l8-7M30 27l-8-7" fill="none" stroke="var(--card)" stroke-width="2"/>
      </svg>
      <span class="icon-row__rule"></span>
    </div>
    <div class="contact">
      <div>+61 3 9040 2267</div>
      <div>1800 374 915</div>
      <div>www.gombrevo.com.au</div>
      <div>sales@gombrevo.com.au</div>
    </div>
    <div class="divider"></div>
    <div class="address">
      <div>4/22 Calder Lane</div>
      <div>Kew Hill Vic 3188</div>
    </div>
  </section>

  <section class="card card--back">
    <div class="pattern-field" role="img" aria-label="Faint repeated brand wordmark pattern in glossy black on black"></div>
    <div class="wordmark">Gombrevo</div>
    <div class="slogan">Your furry friends<br>deserves the best</div>
  </section>
</body>
</html>
```